Craft Beer Needs a Label/ Logo Design

Name: Lanternfall
(Lanternfall Ale, Lanternfall Pilsner, Lanternfall Stout)

We are looking for a logo-ed label that will resonate domestically and internationally for this new Craft Beer Brand.

Target Market(s)

Millenials

Logo Text

Lanternfall Pilsner

Logo styles of interest
Emblem Logo
Character Logo
Colors

Designer to choose colors to be used in the design.

Requirements
Must have
• A labled logo design -- "Lanternfall" is the name, but would like to see samples with "Ale", "Pilsner", or "Stout" after!

```html
<!DOCTYPE html>
<html lang="en">
<head>
<meta charset="utf-8">
<title>Lanternfall Pilsner Label</title>
<link rel="stylesheet" href="https://fonts.googleapis.com/css2?family=Cinzel:wght@400;700&family=Fira+Sans:wght@400;700&family=Fira+Sans+Condensed:wght@800&display=swap">
<style>
  :root {
    --page: #ffffff;
    --backdrop: #f3f3f3;
    --navy: #0c2a44;
    --navy-deep: #081f34;
    --steel: #7e9fb8;
    --steel-light: #9bb6ca;
    --gold: #f4b646;
    --band: #f6c86c;
    --band-light: #fbd98f;
    --white: #ffffff;
  }
  html, body {
    margin: 0;
    width: 1200px;
    height: 903px;
    overflow: hidden;
    background: var(--page);
  }
  .canvas {
    position: relative;
    width: 1200px;
    height: 903px;
  }
  .backdrop {
    position: absolute;
    left: 60px; top: 60px;
    width: 1080px; height: 770px;
    background: var(--backdrop);
  }
  .label {
    position: absolute;
    left: 0; top: 0;
  }
  .brand-name { font-family: "Cinzel", serif; font-size: 42px; fill: var(--white); letter-spacing: 1px; }
  .brand-sub { font-family: "Fira Sans", sans-serif; font-weight: 700; font-size: 22px; fill: var(--gold); }
  .spec { font-family: "Fira Sans", sans-serif; font-size: 16px; fill: var(--white); }
  .style-name { font-family: "Fira Sans Condensed", sans-serif; font-weight: 800; font-size: 92px; fill: var(--navy); }
  .style-kind { font-family: "Cinzel", serif; font-size: 31px; fill: var(--white); }
  .origin { font-family: "Cinzel", serif; font-weight: 700; font-size: 13px; fill: var(--gold); }
</style>
</head>
<body>
<div class="canvas">
  <div class="backdrop"></div>
  <svg class="label" width="1200" height="903" viewBox="0 0 1200 903">
    <defs>
      <radialGradient id="glow" cx="50%" cy="78%" r="60%">
        <stop offset="0" stop-color="#2d5275"/>
        <stop offset="1" stop-color="#0c2a44"/>
      </radialGradient>
      <linearGradient id="emblemFill" x1="0" y1="0" x2="0" y2="1">
        <stop offset="0" stop-color="#a9c2d5"/>
        <stop offset="1" stop-color="#2b4c69"/>
      </linearGradient>
    </defs>

    <!-- outer label frame -->
    <path class="label-frame" d="M160 205 L340 145 Q350 142 360 145 L540 205 Q553 210 553 224 L553 648 Q553 658 543 662 L356 727 Q350 729 344 727 L157 662 Q147 658 147 648 L147 224 Q147 210 160 205 Z"
          fill="var(--steel)" stroke="var(--navy)" stroke-width="4"/>

    <!-- inner dark panel -->
    <path class="label-panel" d="M172 265 L340 218 Q350 215 360 218 L528 265 Q538 268 538 280 L538 612 Q538 620 530 623 L356 668 Q350 670 344 668 L170 623 Q162 620 162 612 L162 280 Q162 268 172 265 Z"
          fill="url(#glow)"/>

    <!-- emblem roundel -->
    <circle class="emblem-ring" cx="350" cy="192" r="58" fill="var(--navy)"/>
    <circle cx="350" cy="192" r="52" fill="var(--gold)"/>
    <circle cx="350" cy="192" r="48" fill="url(#emblemFill)" role="img" aria-label="Brand emblem: night sky roundel"/>

    <!-- brand lettering -->
    <text class="brand-name" x="350" y="300" text-anchor="middle">LANTERNFALL</text>
    <text class="brand-sub" x="350" y="325" text-anchor="middle">CRAFT BEERS</text>

    <!-- specs -->
    <text class="spec" x="182" y="428">355mL</text>
    <text class="spec" x="520" y="428" text-anchor="end">ALC 3.7% Vol</text>

    <!-- ribbon -->
    <g class="ribbon">
      <path d="M133 458 L152 448 L152 562 L133 555 Z" fill="var(--navy)"/>
      <path d="M567 441 L548 448 L548 562 L567 555 Z" fill="var(--navy)"/>
      <path d="M136 460 L152 452 L152 558 L136 552 Z" fill="var(--band)"/>
      <path d="M564 444 L548 452 L548 558 L564 552 Z" fill="var(--band)"/>
      <rect x="150" y="446" width="400" height="116" fill="var(--band)" stroke="var(--navy)" stroke-width="4"/>
      <text class="style-name" x="350" y="537" text-anchor="middle">PILSNER</text>
    </g>

    <!-- style & origin -->
    <text class="style-kind" x="350" y="595" text-anchor="middle">PREMIUM LAGER</text>
    <text class="origin" x="350" y="620" text-anchor="middle">BOTTLED IN ARIZONA, USA</text>
  </svg>
</div>
</body>
</html>
```